Looking for a modern, Professional business card design

We have a simple business card, but are looking for a more modern, professional look. A sample of the basic card is attached as well as the logo. We would also like to add that we offer:
Struggling with your finances?
- Learn to become debt free
- Discover the power of cash
- Control your money instead of it controlling you
Let us help you achieve a new level of financial freedom!
Also, we would like to have a "SPECIAL OFFER!: FREE 30 minute consultation"
Financial Planning

```html
<!DOCTYPE html>
<html lang="en">
<head>
<meta charset="utf-8">
<title>Clearpath Coaching – Business Card</title>
<link rel="stylesheet" href="https://fonts.googleapis.com/css2?family=Arimo:wght@400;700&display=swap">
<style>
  :root {
    --bg: #4a423d;
    --card: #1b1b1b;
    --green: #5fb83a;
    --white: #f2f2f2;
    --rule: #8a8a8a;
  }
  * { box-sizing: border-box; margin: 0; padding: 0; }
  html, body {
    width: 1200px; height: 787px; overflow: hidden;
    background: var(--bg);
    font-family: "Arimo", Arial, sans-serif;
  }
  .stage {
    position: relative; width: 1200px; height: 787px;
    display: flex; align-items: center; justify-content: center; gap: 40px;
  }
  .card {
    position: relative;
    width: 540px; height: 309px;
    background: var(--card);
    border-radius: 4px;
    box-shadow: 0 10px 24px rgba(0,0,0,.35);
    color: var(--white);
  }
  .brand-name {
    font-weight: 700; color: var(--white);
    line-height: 1.1; letter-spacing: 1px;
  }

  /* Offer side */
  .card-offer { padding: 34px 34px; text-align: center; }
  .card-offer .brand-name { font-size: 28px; }
  .offer-heading {
    margin-top: 26px; color: var(--green);
    font-weight: 700; font-size: 15px; letter-spacing: .3px;
  }
  .offer-list { margin-top: 8px; font-size: 13px; line-height: 1.5; }
  .offer-list .sep { color: var(--green); padding: 0 6px; }
  .offer-cta {
    margin-top: 22px; font-weight: 700; font-size: 16px; text-align: left;
  }

  /* Contact side */
  .contact-person { position: absolute; left: 34px; top: 46px; }
  .person-name { color: var(--green); font-size: 19px; font-weight: 400; }
  .person-role { font-size: 15px; margin-top: 4px; }
  .contact-list { list-style: none; margin-top: 12px; font-size: 14px; }
  .contact-list li { display: flex; align-items: center; gap: 10px; line-height: 1.65; }
  .contact-list svg { width: 12px; height: 12px; flex: none; }
  .card-contact .brand-name {
    position: absolute; right: 30px; top: 92px;
    font-size: 24px; text-align: right;
  }
  .contact-rule {
    position: absolute; left: 34px; right: 30px; bottom: 58px;
    height: 1px; background: var(--rule);
  }
</style>
</head>
<body>
<main class="stage">

  <section class="card card-offer">
    <p class="brand-name">CLEARPATH COACHING</p>
    <h2 class="offer-heading">STRUGGLING WITH YOUR FINANCES?</h2>
    <p class="offer-list">
      Learn to become debt free<span class="sep">•</span>Discover the power of cash<br>
      Control your money instead of it controlling you<br>
      Let us help you achieve a new level of financial freedom!
    </p>
    <p class="offer-cta">SPECIAL OFFER!: FREE 30 minute consultation</p>
  </section>

  <section class="card card-contact">
    <div class="contact-person">
      <h1 class="person-name">Daniel R. Hughes</h1>
      <p class="person-role">Personal Financial Coach</p>
      <ul class="contact-list">
        <li>
          <svg viewBox="0 0 12 12" aria-hidden="true"><rect x="3" y="0.5" width="6" height="11" rx="1" fill="var(--green)"/><rect x="4" y="2" width="4" height="7" fill="var(--card)"/></svg>
          (555) 014-2283
        </li>
        <li>
          <svg viewBox="0 0 12 12" aria-hidden="true"><rect x="0.5" y="2" width="11" height="8" rx="1" fill="var(--green)"/><path d="M1 2.5 L6 6.5 L11 2.5" stroke="var(--card)" stroke-width="1" fill="none"/></svg>
          daniel@clearpathmoneycoach.com
        </li>
        <li>
          <svg viewBox="0 0 12 12" aria-hidden="true"><circle cx="6" cy="6" r="5.5" fill="var(--green)"/><ellipse cx="6" cy="6" rx="2.3" ry="5" fill="none" stroke="var(--card)" stroke-width=".9"/><line x1="1" y1="6" x2="11" y2="6" stroke="var(--card)" stroke-width=".9"/></svg>
          www.clearpathmoneycoach.com
        </li>
      </ul>
    </div>
    <p class="brand-name">CLEARPATH<br>COACHING</p>
    <div class="contact-rule"></div>
  </section>

</main>
</body>
</html>
```